Book cover for LM

Design cover for a book of gratitude and inspiration.
Book trim size will be 6.5 x 6.5 inches, or 8 x 8 inches, hardcover, 96 pages
Title: Lantern Meadows
Subtitle: A Book of Gratitude and Inspiration
Author: Gus Halverd

```html
<!DOCTYPE html>
<html lang="en">
<head>
<meta charset="UTF-8">
<title>Lantern Meadows — Book Cover</title>
<link rel="stylesheet" href="https://fonts.googleapis.com/css2?family=Cinzel:wght@400&family=Josefin+Sans:wght@600&family=Marcellus&display=swap">
<style>
  :root {
    --sky-violet: #66588a;
    --sky-mauve: #9c6284;
    --sky-rose: #c8707e;
    --sky-coral: #e98c72;
    --sky-amber: #f5a85c;
    --sky-gold: #f7d35a;
    --sky-glow: #f7e46a;
    --ground-shadow: #2a1c0c;
    --ground-deep: #120c05;
    --gold-light: #fdf0b0;
    --gold-mid: #f7cf6a;
    --gold-deep: #eeae3e;
    --gold-edge: #8a5a1e;
    --cream: #fbefb6;
  }
  * { margin: 0; padding: 0; box-sizing: border-box; }
  html, body {
    width: 1200px;
    height: 1200px;
    overflow: hidden;
    background: var(--ground-deep);
  }
  .cover {
    position: relative;
    width: 1200px;
    height: 1200px;
    overflow: hidden;
  }
  .cover-photo {
    position: absolute;
    inset: 0;
    background: linear-gradient(180deg,
      var(--sky-violet) 0%,
      var(--sky-mauve) 20%,
      var(--sky-rose) 36%,
      var(--sky-coral) 50%,
      var(--sky-amber) 62%,
      var(--sky-gold) 72%,
      var(--sky-glow) 78%,
      var(--sky-gold) 81%,
      var(--ground-shadow) 84%,
      var(--ground-deep) 100%);
  }
  .cover-type {
    position: absolute;
    inset: 0;
    width: 1200px;
    height: 1200px;
  }
  .title {
    font-family: "Cinzel", serif;
    font-weight: 400;
    fill: url(#gold-fill);
    stroke: var(--gold-edge);
    stroke-width: 1.2;
    paint-order: stroke;
  }
  .subtitle {
    font-family: "Josefin Sans", sans-serif;
    font-weight: 600;
    fill: var(--cream);
  }
  .author {
    font-family: "Marcellus", serif;
    fill: var(--cream);
  }
</style>
</head>
<body>
  <main class="cover">
    <div class="cover-photo" role="img" aria-label="Photograph of a person in silhouette with arms spread wide, standing in tall grass against a violet, pink and golden sunset sky"></div>

    <svg class="cover-type" viewBox="0 0 1200 1200" xmlns="http://www.w3.org/2000/svg">
      <defs>
        <linearGradient id="gold-fill" x1="0" y1="0" x2="0" y2="1">
          <stop offset="0%" stop-color="var(--gold-light)"/>
          <stop offset="55%" stop-color="var(--gold-mid)"/>
          <stop offset="100%" stop-color="var(--gold-deep)"/>
        </linearGradient>
      </defs>

      <text class="title title-line-one" x="93" y="238" font-size="160" textLength="994" lengthAdjust="spacingAndGlyphs">LANTERN</text>
      <text class="title title-line-two" x="300" y="430" font-size="168" textLength="787" lengthAdjust="spacingAndGlyphs">MEADOWS</text>

      <text class="subtitle" x="371" y="488" font-size="34" textLength="713" lengthAdjust="spacingAndGlyphs">A BOOK OF GRATITUDE AND INSPIRATION</text>

      <text class="author" x="422" y="1140" font-size="66" textLength="356" lengthAdjust="spacingAndGlyphs">GUS HALVERD</text>
    </svg>
  </main>
</body>
</html>
```